Business Card Design for Kidvale (Hires out childrens play areas)

Looking to have a business card designed for a company we just bought. The company rents out childrens play areas.

I have uploaded a couple of examples of the kind of business card style I like. Here are two more examples:

https://quorvastudio.nz/project/bright-romp-branding/
https://imgvaultcdn.com/design_img/8841052/302917/302917_5518203_8841052_b73e19a2_image.jpg

I think a white card will be best due to all the colours in the logo.

Size we require: 3.75" x 2.25" (horizontally orientated) with a 0.125" bleed

Uploaded is two versions of our logo.

Details for the card:
1. My name: Liam Verster
2. Title: Managing Director
3. Phone no: 021 563 417
4. Email: liam@kidvale.co.nz
5. URL: www.kidvale.co.nz
6. Address:
PO Box 318625
Fernlea, Auckland

Let me know if you need anything else.

Target Market(s)

Hospitals, doctors surgeries, bed shops, etc.

Contact Information for Business Card

Details for the card:
1. My name: Liam Verster
3. Phone no: 021 563 417
5. URL: www.kidvale.co.nz
6. Address:
PO Box 318625
Fernlea, Auckland

Requirements
Should not have
• Not too busy.

```html
<!DOCTYPE html>
<html lang="en">
<head>
<meta charset="utf-8">
<title>Kidvale Business Card</title>
<link rel="stylesheet" href="https://fonts.googleapis.com/css2?family=Hind:wght@500;600;700&display=swap">
<style>
  :root {
    --canvas: #e9eeec;
    --card: #ffffff;
    --ink-blue: #1f4fa0;
    --block-teal: #1fa3a6;
    --block-red: #e0262c;
    --block-green: #3aa83c;
    --block-orange: #f7931e;
    --icon-orange: #f39a1f;
    --icon-green: #3aa83c;
    --icon-red: #e0262c;
    --icon-teal: #1f9fb0;
    --faint-pattern: #f3f2f7;
    --trim: #f08a4b;
  }
  * { box-sizing: border-box; margin: 0; padding: 0; }
  html, body {
    width: 1200px; height: 1200px; overflow: hidden;
    background: var(--canvas);
    font-family: "Hind", Arial, sans-serif;
  }
  .sheet {
    width: 1200px; height: 1200px;
    display: flex; flex-direction: column; align-items: center; justify-content: center;
    gap: 40px;
  }
  .card {
    position: relative;
    width: 900px; height: 540px;
    background: var(--card);
    overflow: hidden;
    box-shadow: 0 2px 10px rgba(0,0,0,0.08);
  }
  .block-band {
    position: absolute; left: 0; width: 100%;
    background: linear-gradient(90deg,
      var(--block-teal) 0%, var(--block-red) 18%, var(--block-green) 36%,
      var(--block-orange) 52%, var(--block-teal) 66%, var(--block-red) 80%, var(--block-orange) 100%);
  }
  .block-band--top { top: 0; height: 44px; border-radius: 0 0 10px 10px; }
  .block-band--bottom { bottom: 0; height: 54px; border-radius: 10px 10px 0 0; }

  .brand {
    position: absolute;
    display: flex; align-items: center; gap: 14px;
    color: var(--ink-blue); font-weight: 700;
  }
  .brand__dot { border-radius: 50%; background: var(--block-orange); flex: none; }
  .card--front .brand { left: 62px; top: 232px; font-size: 62px; }
  .card--front .brand__dot { width: 36px; height: 36px; }

  .contact {
    position: absolute; left: 508px; top: 100px;
    color: var(--ink-blue);
  }
  .contact__name { font-size: 44px; font-weight: 700; line-height: 1; }
  .contact__title { font-size: 25px; font-weight: 600; margin-top: 8px; }
  .contact__row {
    display: flex; align-items: flex-start; gap: 20px;
    font-size: 27px; font-weight: 600; line-height: 1.3;
  }
  .contact__row svg { width: 32px; height: 32px; flex: none; margin-top: 2px; }
  .contact__address { margin-top: 30px; }
  .contact__list { margin-top: 38px; display: flex; flex-direction: column; gap: 8px; }

  .card--back .pattern {
    position: absolute; inset: 0;
    background: var(--faint-pattern);
  }
  .card--back .brand {
    left: 50%; top: 50%; transform: translate(-50%, -50%);
    font-size: 84px;
  }
  .card--back .brand__dot { width: 48px; height: 48px; }
</style>
</head>
<body>
<main class="sheet">
  <section class="card card--front">
    <div class="block-band block-band--top" role="img" aria-label="Row of colourful toy blocks"></div>

    <div class="brand">
      <span class="brand__dot"></span>
      <span class="brand__name">Kidvale</span>
    </div>

    <div class="contact">
      <h1 class="contact__name">Liam Verster</h1>
      <p class="contact__title">Managing Director</p>

      <div class="contact__row contact__address">
        <svg viewBox="0 0 32 32" aria-hidden="true">
          <path d="M16 3a8 8 0 0 0-8 8c0 6 8 14 8 14s8-8 8-14a8 8 0 0 0-8-8z" fill="var(--icon-orange)"/>
          <circle cx="16" cy="11" r="3" fill="#fff"/>
          <ellipse cx="16" cy="28" rx="8" ry="2.2" fill="none" stroke="var(--icon-orange)" stroke-width="2"/>
        </svg>
        <p>PO Box 318625<br>Fernlea, Auckland</p>
      </div>

      <div class="contact__list">
        <div class="contact__row">
          <svg viewBox="0 0 32 32" aria-hidden="true">
            <path d="M9 5l4 5-2.5 3a14 14 0 0 0 8.5 8.5l3-2.5 5 4-3 4C14 27 5 18 5 8z" fill="var(--icon-green)"/>
            <path d="M19 6a8 8 0 0 1 7 7M19 10a4 4 0 0 1 3 3" fill="none" stroke="var(--icon-green)" stroke-width="2" stroke-linecap="round"/>
          </svg>
          <p>021 563 417</p>
        </div>
        <div class="contact__row">
          <svg viewBox="0 0 32 32" aria-hidden="true">
            <rect x="4" y="8" width="24" height="16" fill="none" stroke="var(--icon-red)" stroke-width="2.2"/>
            <path d="M4 8l12 10 12-10" fill="none" stroke="var(--icon-red)" stroke-width="2.2"/>
          </svg>
          <p>liam@kidvale.co.nz</p>
        </div>
        <div class="contact__row">
          <svg viewBox="0 0 32 32" aria-hidden="true">
            <circle cx="16" cy="16" r="11" fill="none" stroke="var(--icon-teal)" stroke-width="2"/>
            <ellipse cx="16" cy="16" rx="5" ry="11" fill="none" stroke="var(--icon-teal)" stroke-width="2"/>
            <path d="M5 16h22M7 10h18M7 22h18" stroke="var(--icon-teal)" stroke-width="2"/>
          </svg>
          <p>www.kidvale.co.nz</p>
        </div>
      </div>
    </div>

    <div class="block-band block-band--bottom" role="img" aria-label="Row of colourful toy blocks"></div>
  </section>

  <section class="card card--back">
    <div class="pattern" role="img" aria-label="Faint repeating pattern of the brand character"></div>
    <div class="brand">
      <span class="brand__dot"></span>
      <span class="brand__name">Kidvale</span>
    </div>
  </section>
</main>
</body>
</html>
```